Looking for Landingpage / Website Designer

We are looking for a Web Designer / Developer for our upcoming Start Up Websites. The first project will be a simple responsive business website with a CTA- Button and an optional Newsletter Opt-In. We do aim for a modern online business approach, since we are a young company.

It is necessary to understand, that we need a conversion orientated design, not a wordpress blog with widgets and galleries.

We are currently discussing how it is going to happen and what preferences we need to focus on.

What we know is, that it should be more of a landing page with an option of adding 2 or 3 Navigation points.

We even thought about using services like plumvesta.com or crintofold.com to have an easier approach for future customizations and A/B testing.

We'd love to see how you fit the design/colors to the upcoming logo
(which is not the final version yet )

hope you can do something about that.

For the Structure.

1. Bracket

Slogan plus a preview text of what we are offering. On the right side a video placeholder plus CTA button.

2. Bracket

Illustrating 3 Benefits. On the right side - Opt in for Contact/Newsletter and CTA Button

3. Bracket

Picture with text just like you have it with the testimonial

You can orientate yourself towards to that landing page example as well:

http://cdn2.zorvellink.net/hub/53/file-581676469-png/Blog-Related_Images/plumvesta_landing_page.png?t=1416543075530

If our collaboration is going well, we would like to stay in touch for further projects.
Updates

Reason: There are 3 Design we do really like but, don't fit exactly our needs. 5 Days max.

Reason: For final adjustments.

I just uploaded the final logo :) Thank you for your commitment so far!

Target Market(s)

Our targeted audience could be almost everybody, who looks for an average paid side job (students, unemployed, house wives and whatever you can imagine). Maybe this is enough information for you to get a mere perception of what this is all about.

Industry/Entity Type

Business

Coding

Coded - Design and coding required

Font styles to use
Serif
Sans Serif

Colors
acd037
5c5c5c
33a6d7

Requirements
Must have
• Registration Opt-In
Responsive on any Device
Customizable
A benefits navigation just like in that example I've uploaded.
Nice to have
• As fast as possible ;D

```html
<!DOCTYPE html>
<html lang="en">
<head>
<meta charset="utf-8">
<title>Taskvolo.de</title>
<link href="https://fonts.googleapis.com/css2?family=Lato:ital,wght@0,400;0,700;0,900;1,400;1,700&display=swap" rel="stylesheet">
<style>
:root{
  --green:#acd037;
  --dark:#5c5c5c;
  --blue:#33a6d7;
  --sky:#4eb1dd;
  --sky-deep:#3f9fcf;
  --grey:#e4e4e4;
  --text:#444;
  --white:#fff;
}
*{box-sizing:border-box;margin:0;padding:0}
html,body{width:1024px;height:1200px;overflow:hidden}
body{font-family:'Lato',sans-serif;color:var(--text);position:relative;background:var(--white)}

.hero{position:absolute;left:0;top:0;width:1024px;height:472px;
  background:linear-gradient(135deg,#5bbbe4 0%,var(--sky) 40%,var(--sky-deep) 70%,#57b5e0 100%)}
.topbar{position:absolute;left:119px;top:0;width:785px;height:86px;background:var(--white)}
.brand{position:absolute;left:24px;top:20px;display:flex;align-items:center;gap:10px}
.brand-dot{width:44px;height:44px;border-radius:50%;background:var(--green)}
.brand-name{font-size:40px;font-weight:900;color:var(--green);letter-spacing:-1px}
.nav{position:absolute;left:413px;top:0;height:86px;display:flex}
.nav a{display:block;padding:0 8px;line-height:80px;font-size:14px;font-weight:700;color:var(--dark);text-decoration:none}
.nav a.active{background:var(--dark);color:var(--white)}

.slide-arrow{position:absolute;top:262px;width:36px;height:36px;background:var(--dark);display:flex;align-items:center;justify-content:center}
.slide-arrow.prev{left:0}.slide-arrow.next{right:0}

.hero-title{position:absolute;left:134px;top:148px;font-size:58px;font-weight:700;color:var(--white);letter-spacing:-1px}
.hero-text{position:absolute;left:135px;top:223px;width:365px;font-size:14px;line-height:21px;font-weight:700;color:var(--white);text-align:justify}
.cta{position:absolute;left:136px;top:354px;width:157px;height:36px;background:var(--white);border-radius:2px;color:var(--blue);font-size:19px;font-style:italic;font-weight:400;display:flex;align-items:center;justify-content:center}
.video{position:absolute;left:519px;top:157px;width:369px;height:234px;background:var(--white);padding:6px}
.video-screen{width:100%;height:100%;background:radial-gradient(circle at 50% 45%,#6a6a6a,#2a2a2a 75%);position:relative}
.video-bar{position:absolute;left:0;right:0;bottom:0;height:20px;background:#1b1b1b}
.video-bar .progress{position:absolute;left:0;top:0;height:3px;width:24%;background:#d22}

.benefits{position:absolute;left:0;top:472px;width:1024px;height:311px;background:var(--grey)}
.card{position:absolute;top:36px;width:177px;height:233px;background:var(--dark);border-radius:2px;text-align:center;color:var(--white)}
.card-icon{width:84px;height:76px;margin:15px auto 0;background:var(--blue);border:2px solid var(--white);border-radius:3px;display:flex;align-items:center;justify-content:center}
.card h3{font-size:13.5px;font-weight:700;margin-top:15px;letter-spacing:.2px}
.card p{font-size:10.5px;line-height:13.6px;margin-top:10px;padding:0 1px}
.btn{display:inline-flex;align-items:center;justify-content:center;background:var(--blue);color:var(--white);font-size:14px;font-weight:700;height:28px;border-radius:2px}
.card .btn{width:86px;margin-top:8px}
.signup{text-align:left}
.signup h3{font-size:16px;margin:10px 0 0 9px;letter-spacing:0}
.field{display:block;width:158px;height:28px;margin:0 0 6px 9px;background:var(--white);border:none;border-radius:2px;font-family:inherit;font-size:12px;font-style:italic;color:#7a7a7a;padding-left:7px;line-height:28px}
.signup form{margin-top:14px}
.signup .btn{width:86px;margin:8px 0 0 46px;height:29px}

.testimonials{position:absolute;left:0;top:783px;width:1024px;height:374px}
.testimonials h2{position:absolute;left:137px;top:18px;font-size:20px;font-style:italic;font-weight:700;color:#3a3a3a}
.quote{position:absolute;width:380px;height:140px}
.quote h4{font-size:15px;font-weight:700;color:#4a4a4a}
.quote h4 span{color:var(--blue)}
.avatar{position:absolute;left:0;top:27px;width:87px;height:87px;border-radius:50%;border:2px solid #3a3a3a;background:radial-gradient(circle at 50% 40%,#c8c8c8,#8a8f98)}
.bubble{position:absolute;left:111px;top:20px;width:255px;height:102px;background:var(--grey);font-size:10.5px;line-height:13.5px;color:#555;text-align:justify;padding:15px 22px 0 27px}
.bubble::before{content:"";position:absolute;left:-18px;top:26px;border:10px solid transparent;border-right-color:var(--grey);border-width:10px 18px 10px 0}
.bubble .open,.bubble .close{position:absolute;font-family:Georgia,serif;font-size:28px;font-weight:700;color:#aaa;line-height:1}
.bubble .open{left:5px;top:6px}.bubble .close{right:4px;bottom:2px}

.footer{position:absolute;left:0;top:1157px;width:1024px;height:43px;background:var(--dark);color:var(--white);font-size:14px;font-style:italic;font-weight:700;display:flex;align-items:center;justify-content:center}
</style>
</head>
<body>

<section class="hero">
  <header class="topbar">
    <div class="brand"><span class="brand-dot"></span><span class="brand-name">Taskvolo.de</span></div>
    <nav class="nav">
      <a class="active" href="#">Home</a>
      <a href="#">About Us</a>
      <a href="#">Services</a>
      <a href="#">Testimonial</a>
      <a href="#">Contact Us</a>
    </nav>
  </header>

  <div class="slide-arrow prev"><svg width="14" height="12" viewBox="0 0 14 12"><path d="M7 1 2 6l5 5M12 1 7 6l5 5" fill="none" stroke="var(--blue)" stroke-width="1.8"/></svg></div>
  <div class="slide-arrow next"><svg width="14" height="12" viewBox="0 0 14 12"><path d="M2 1l5 5-5 5M7 1l5 5-5 5" fill="none" stroke="var(--blue)" stroke-width="1.8"/></svg></div>

  <h1 class="hero-title">Taskvolo.de</h1>
  <p class="hero-text">Lorem Ipsum is simply dummy text of the printing and typesetting industry. Lorem Ipsum has been the industry's standard dummy text ever since the 1500s, when an unknown printer took a galley of type and scrambled it to make a type specimen book.</p>
  <div class="cta">Get Stared Now</div>

  <div class="video">
    <div class="video-screen" role="img" aria-label="Video placeholder: presenter seated in a studio under desk lamps">
      <div class="video-bar"><div class="progress"></div></div>
    </div>
  </div>
</section>

<section class="benefits">
  <div class="card" style="left:135px">
    <div class="card-icon"><svg width="46" height="44" viewBox="0 0 46 44" fill="none" stroke="#fff" stroke-width="6"><path d="M14 18 21 7h4l6 10"/><path d="M33 25l6 10-3 4H25"/><path d="M18 39H9l-3-4 5-9"/></svg></div>
    <h3>LOREM IPSUM IS SIMPLY</h3>
    <p>Dummy text of the printing and typesetting industry. Lorem Ipsum has been the industry's standard dummy text ever since the 1500s,</p>
    <span class="btn">Read More</span>
  </div>
  <div class="card" style="left:327px">
    <div class="card-icon"><svg width="32" height="42" viewBox="0 0 32 42"><path d="M8 20v-9a8 8 0 0 1 16 0v2" fill="none" stroke="#fff" stroke-width="5"/><rect x="2" y="20" width="28" height="20" rx="2" fill="#fff"/></svg></div>
    <h3>LOREM IPSUM IS SIMPLY</h3>
    <p>Dummy text of the printing and typesetting industry. Lorem Ipsum has been the industry's standard dummy text ever since the 1500s,</p>
    <span class="btn">Read More</span>
  </div>
  <div class="card" style="left:519px">
    <div class="card-icon"><svg width="50" height="46" viewBox="0 0 50 46" fill="#fff"><circle cx="10" cy="11" r="6"/><circle cx="40" cy="11" r="6"/><circle cx="25" cy="14" r="8"/><path d="M0 30a10 8 0 0 1 20 0v4H0z"/><path d="M30 30a10 8 0 0 1 20 0v4H30z"/><path d="M10 40a15 13 0 0 1 30 0v6H10z"/></svg></div>
    <h3>LOREM IPSUM IS SIMPLY</h3>
    <p>Dummy text of the printing and typesetting industry. Lorem Ipsum has been the industry's standard dummy text ever since the 1500s,</p>
    <span class="btn">Read More</span>
  </div>
  <div class="card signup" style="left:711px">
    <h3>Free Consultion Signup</h3>
    <form>
      <span class="field">Your Name</span>
      <span class="field">Email Address</span>
      <span class="field">Company Name</span>
      <span class="field">Phone</span>
      <span class="btn">Submit</span>
    </form>
  </div>
</section>

<section class="testimonials">
  <h2>What Our Customers Have To Say</h2>

  <div class="quote" style="left:137px;top:62px">
    <h4><span>Arlen Dovitch</span> - Director Of Company Name</h4>
    <div class="avatar" role="img" aria-label="Portrait of Arlen Dovitch"></div>
    <div class="bubble"><span class="open">“</span>When an unknown printer took a galley of type and scrambled it to make a type specimen book. It has survived not only five centuries, but also the leap into electronic typesetting<span class="close">”</span></div>
  </div>
  <div class="quote" style="left:521px;top:62px">
    <h4><span>Jonas Pellard</span> - Director Of Company Name</h4>
    <div class="avatar" role="img" aria-label="Portrait of Jonas Pellard"></div>
    <div class="bubble"><span class="open">“</span>When an unknown printer took a galley of type and scrambled it to make a type specimen book. It has survived not only five centuries, but also the leap into electronic typesetting<span class="close">”</span></div>
  </div>
  <div class="quote" style="left:137px;top:219px">
    <h4><span>Arlen Dovitch</span> - Director Of Company Name</h4>
    <div class="avatar" role="img" aria-label="Portrait of Arlen Dovitch"></div>
    <div class="bubble"><span class="open">“</span>When an unknown printer took a galley of type and scrambled it to make a type specimen book. It has survived not only five centuries, but also the leap into electronic typesetting<span class="close">”</span></div>
  </div>
  <div class="quote" style="left:521px;top:219px">
    <h4><span>Jonas Pellard</span> - Director Of Company Name</h4>
    <div class="avatar" role="img" aria-label="Portrait of Jonas Pellard"></div>
    <div class="bubble"><span class="open">“</span>When an unknown printer took a galley of type and scrambled it to make a type specimen book. It has survived not only five centuries, but also the leap into electronic typesetting<span class="close">”</span></div>
  </div>
</section>

<footer class="footer">Built Using the Plumvesta Landing Page</footer>

</body>
</html>
```